New Company Business Card design

Looking for a corporate looking business card utilising my new logo design - the logo i would like embossed as one option and flat as another - simplistic but stylish - less is more - we are an import export business launching into the market - i would like a couple of options as main background - Grey or Black

```html
<!DOCTYPE html>
<html lang="en">
<head>
<meta charset="utf-8">
<title>Meridian Trade Partners – Business Card</title>
<link rel="stylesheet" href="https://fonts.googleapis.com/css2?family=Open+Sans:wght@400;600;700&display=swap">
<style>
  :root {
    --backdrop: #2b2b2d;
    --card: #ffffff;
    --brand-blue: #2a72c0;
    --brand-grey: #6f7175;
    --ink: #2e2e30;
    --rule: #c9cacc;
    --card-shadow: rgba(0, 0, 0, 0.45);
  }
  * { box-sizing: border-box; margin: 0; padding: 0; }
  html, body {
    width: 1200px;
    height: 900px;
    overflow: hidden;
    background: var(--backdrop);
    font-family: "Open Sans", Arial, sans-serif;
  }
  .canvas {
    position: relative;
    width: 1200px;
    height: 900px;
  }
  .card {
    position: absolute;
    left: 290px;
    width: 620px;
    height: 354px;
    background: var(--card);
    border-radius: 16px;
    overflow: hidden;
    box-shadow: 0 14px 30px var(--card-shadow);
  }
  .card--front { top: 70px; }
  .card--back { top: 476px; }

  .brand {
    display: flex;
    align-items: center;
    gap: 10px;
    color: var(--brand-blue);
    font-weight: 600;
    letter-spacing: 0.04em;
    text-transform: uppercase;
    line-height: 1.15;
  }
  .brand__dot {
    flex: none;
    border-radius: 50%;
    background: var(--brand-blue);
  }

  /* front */
  .front__brand {
    position: absolute;
    left: 34px;
    top: 140px;
    width: 250px;
    font-size: 19px;
  }
  .front__brand .brand__dot { width: 16px; height: 16px; }
  .front__divider {
    position: absolute;
    left: 300px;
    top: 56px;
    width: 1px;
    height: 190px;
    background: var(--rule);
  }
  .contact {
    position: absolute;
    left: 328px;
    top: 58px;
    color: var(--ink);
    font-size: 15px;
    line-height: 1.35;
  }
  .contact__name {
    color: var(--brand-blue);
    font-weight: 700;
    font-size: 18px;
  }
  .contact__role { margin-bottom: 12px; }
  .contact__address { margin-bottom: 12px; }
  .contact__line {
    display: flex;
    align-items: center;
    gap: 8px;
  }
  .contact__icon { width: 12px; height: 12px; flex: none; }
  .web-band {
    position: absolute;
    right: 0;
    bottom: 0;
    width: 290px;
    height: 50px;
    background: var(--brand-blue);
    border-top-left-radius: 22px;
    color: #fff;
    font-size: 16px;
    display: flex;
    align-items: center;
    justify-content: center;
  }

  /* back */
  .back__brand {
    position: absolute;
    left: 0;
    right: 0;
    top: 0;
    bottom: 0;
    justify-content: center;
    font-size: 26px;
  }
  .back__brand .brand__dot { width: 22px; height: 22px; }
</style>
</head>
<body>
<main class="canvas">

  <section class="card card--front" aria-label="Business card front">
    <div class="brand front__brand">
      <span class="brand__dot"></span>
      <span class="brand__name">Meridian Trade Partners</span>
    </div>
    <div class="front__divider"></div>
    <div class="contact">
      <p class="contact__name">Dara Colvin</p>
      <p class="contact__role">Founder/President</p>
      <p class="contact__address">PO Box 418, Quay Street,<br>Port Ellis, 20418</p>
      <p class="contact__line">
        <svg class="contact__icon" viewBox="0 0 12 12" aria-hidden="true">
          <path d="M2.5 1 L4.5 1 L5.2 3.6 L3.9 4.6 Q5 7 7.4 8.1 L8.4 6.8 L11 7.5 L11 9.5 Q10.5 11 9 11 Q1 10 1 2.8 Q1 1.4 2.5 1 Z" fill="var(--brand-blue)"/>
        </svg>
        (555) 014-7720
      </p>
      <p class="contact__line">
        <svg class="contact__icon" viewBox="0 0 12 12" aria-hidden="true">
          <rect x="0.5" y="2" width="11" height="8" fill="var(--brand-blue)"/>
          <path d="M0.5 2 L6 6.5 L11.5 2" fill="none" stroke="#fff" stroke-width="1"/>
        </svg>
        hello@meridiantrade.co
      </p>
    </div>
    <div class="web-band">www.harbourlinetrade.com</div>
  </section>

  <section class="card card--back" aria-label="Business card back">
    <div class="brand back__brand">
      <span class="brand__dot"></span>
      <span class="brand__name">Meridian Trade Partners</span>
    </div>
  </section>

</main>
</body>
</html>
```